Label Design for Climbing Chalk (fitness category)

I am looking for someone to design a front and back label for a bottle of liquid chalk. Liquid chalk is used in gyms, gymnastics, climbing to prevent your hands from getting moist and increase friction. I'm uploading some design motivations that I like.

The bottle is going to be black and I want the label to be clear. You have free reign of how you want to approach this design. Below are more specifics for the sizing:

*Attached is a picture of a competitor product (Tor Hold Liquid Chalk). Please don't use this for motivation, their label is very bad. I'm attaching a picture so that you can see what the bottle looks like.
*Attached are design motivations that I like
*The bottle is 50 ml, it's 3.75 inches tall, 2 inches wide and 1.25 inches in depth.
*The label can be square or oval (it's up to you). The size of the label needs to be 1,25 x 2.25 inches.
*Name of the product: Varnel Liquid Chalk
*Label needs to have the following Required Text. You can arrange it however you like:
- (50 ml)
- Made by USA Competitive Athletes for Athletes. Increases grip and lasts 3-4 times longer than regular chalk.
- Directions: Shake well. Squeeze some Varnel Liquid Chalk into your hand and rub your hands together. Let your hands air dry for about 10 seconds. To remove the chalk wash your hands with light soap.
Warning: Avoid contact with Eyes. Do not use on broken skin. Do not ingest. Keep out of reach of small children.
- Ingredients: Magnesium carbonate, SD Alcohol, hydroxypropylcellulose, colophonium.

Target Market(s)

Fitness, Athletes, Rock Climbers, Weight Lifters, Gymnasts, etc

Industry/Entity Type

Fitness

Font styles to use
Sans Serif

Colors

Designer to choose colors to be used in the design.

Requirements
Must have
• Please see Project Description for required text. The bottle is going to be black and I want the clear label so please be creative with the colors that would look good
Nice to have
• Please see attached branding ideas that I liked for font and colors. You don't have to strictly stick to them, these are just some of the ones I liked. Be creative and put your best foot forward.

```html
<!DOCTYPE html>
<html lang="en">
<head>
<meta charset="utf-8">
<title>Varnel Liquid Chalk – Front and Back Labels</title>
<link href="https://fonts.googleapis.com/css2?family=Archivo:wght@700;800&family=Pathway+Gothic+One&display=swap" rel="stylesheet">
<style>
  :root {
    --bg: #ffffff;
    --label: #000000;
    --ink: #ffffff;
    --accent: #e0161f;
    --badge-grey: #9a9a9a;
    --badge-red: #c8102e;
  }
  * { box-sizing: border-box; margin: 0; padding: 0; }
  html, body {
    width: 1200px;
    height: 1078px;
    overflow: hidden;
    background: var(--bg);
  }
  .canvas {
    position: relative;
    width: 1200px;
    height: 1078px;
  }
  .label {
    position: absolute;
    top: 228px;
    width: 360px;
    height: 623px;
    background: var(--label);
    border-radius: 6px;
    color: var(--ink);
  }
  .label--front { left: 180px; }
  .label--back { left: 660px; }

  /* Front label */
  .front-name {
    position: absolute;
    top: 92px;
    left: 0;
    right: 0;
    text-align: center;
    font-family: "Archivo", sans-serif;
    font-weight: 800;
    color: var(--ink);
    font-size: 50px;
    line-height: 1.02;
    text-transform: uppercase;
  }
  .front-seal {
    position: absolute;
    top: 322px;
    left: 50%;
    margin-left: -52px;
    width: 104px;
    height: 104px;
    border-radius: 50%;
    background: var(--badge-red);
    border: 4px solid var(--ink);
  }
  .front-claim {
    position: absolute;
    top: 444px;
    left: 0;
    right: 0;
    text-align: center;
    font-family: "Archivo", sans-serif;
    font-weight: 700;
    font-size: 23px;
    line-height: 1.18;
  }
  .front-volume {
    position: absolute;
    top: 546px;
    left: 0;
    right: 0;
    text-align: center;
    font-family: "Archivo", sans-serif;
    font-weight: 700;
    font-size: 26px;
    letter-spacing: 0.5px;
  }

  /* Back label */
  .back-body {
    position: absolute;
    top: 36px;
    left: 20px;
    right: 20px;
    font-family: "Pathway Gothic One", sans-serif;
    font-size: 22px;
    line-height: 1.17;
  }
  .back-name {
    font-family: "Archivo", sans-serif;
    font-weight: 800;
    font-size: 26px;
    line-height: 1.02;
    text-transform: uppercase;
    color: var(--ink);
    margin-bottom: 14px;
  }
  .back-headline {
    color: var(--accent);
    font-size: 23px;
    line-height: 1.15;
    margin-bottom: 10px;
  }
  .back-para {
    text-align: justify;
    margin-bottom: 10px;
  }
  .back-para .lead {
    color: var(--accent);
  }
  .back-seal {
    position: absolute;
    right: 26px;
    bottom: 24px;
    width: 122px;
    height: 122px;
    border-radius: 50%;
    background: var(--badge-grey);
    border: 6px solid #5a5a5a;
  }
  .back-seal::after {
    content: "";
    position: absolute;
    inset: 20px;
    border-radius: 50%;
    background: var(--badge-red);
  }
</style>
</head>
<body>
  <main class="canvas">
    <section class="label label--front" aria-label="Front label">
      <h1 class="front-name">Varnel<br>Liquid<br>Chalk</h1>
      <div class="front-seal" role="img" aria-label="Athletes seal"></div>
      <p class="front-claim">Made by USA<br>Competitive Athletes<br>for Athletes</p>
      <p class="front-volume">50 ml</p>
    </section>

    <section class="label label--back" aria-label="Back label">
      <div class="back-body">
        <h2 class="back-name">Varnel Liquid Chalk</h2>
        <p class="back-headline">INCREASES GRIP and lasts 3-4 times longer than regular chalk</p>
        <p class="back-para"><span class="lead">Directions:</span> Shake well. Squeeze some Varnel Liquid Chalk into your hand and rub your hands together. Let your hands air dry for about 10 seconds. To remove the chalk wash your hands with light soap.</p>
        <p class="back-para"><span class="lead">Warning:</span> Avoid contact with Eyes. Do not use on broken skin. Do not ingest. Keep out of reach of small children.</p>
        <p class="back-para"><span class="lead">Ingredients:</span> Magnesium carbonate, SD Alcohol, hydroxypropylcellulose, colophonium.</p>
      </div>
      <div class="back-seal" role="img" aria-label="Origin seal"></div>
    </section>
  </main>
</body>
</html>
```